Stationary for Manufacturing Company
Metal Manufacturing
Stationary for Manufacturing Company - Manufacturing
Creative Brief
Professional
Gerald Pinwick
27615 Harlow Ave Unit C Longmont, CO 80519
gpinwick@forgevx.com
www.forgevx.com
Would like stationary designs following our logo design.
gpinwick gpinwick
quillmotions I like #79 & #87 with the solid color. Can you do a these on other stationary objects.
Nook, I really like the stationary on #88 & #89, can you continue the design onto the inside of the folder on the pockets. Also I would like to see Forge Vexa in shading in smaller text like #16 and the large shaded logo removed. Thank you for your submissions.
#129 & #126 I like both of these cards, #129 seems to have to many lines and seems to busy. Can you reduce some of them and do this on other stationary objects as well. Thank you.
#16 I really like how the text Forge Vexa is on the back of the card.Can you put that one in other stationary objects as well. Thank you.

```html
<!DOCTYPE html>
<html lang="en">
<head>
<meta charset="utf-8">
<title>Forge Vexa — Business Card</title>
<link rel="stylesheet" href="https://fonts.googleapis.com/css2?family=Arimo:wght@400;700&display=swap">
<style>
  :root {
    --backdrop: #d9d9da;
    --card-white: #ffffff;
    --brand-blue: #2c68a6;
    --brand-deep: #1f5590;
    --tagline-light: #7fb3e6;
    --ink: #3a3a3a;
    --icon-grey: #4a4a4a;
  }
  * { margin: 0; padding: 0; box-sizing: border-box; }
  html, body {
    width: 1200px; height: 897px; overflow: hidden;
    background: var(--backdrop);
    font-family: "Arimo", Arial, sans-serif;
  }
  .stage { position: relative; width: 1200px; height: 897px; }

  .card { position: absolute; overflow: hidden; }

  /* Front */
  .card-front {
    left: 274px; top: 32px; width: 664px; height: 404px;
    background: var(--card-white);
  }
  .front-brand {
    position: absolute; left: 0; right: 0; top: 146px; text-align: center;
  }
  .brand-name {
    font-weight: 700; color: var(--brand-blue);
    font-size: 34px; line-height: 1; letter-spacing: -0.5px;
  }
  .brand-tagline {
    font-weight: 400; color: var(--brand-blue);
    font-size: 13px; letter-spacing: 1.6px; margin-top: 3px;
  }
  .person-name {
    position: absolute; left: 0; right: 0; top: 230px; text-align: center;
    font-size: 14px; font-weight: 700; color: var(--brand-blue);
  }
  .contact-list {
    position: absolute; left: 0; right: 0; top: 292px;
    display: flex; flex-direction: column; align-items: center; gap: 8px;
  }
  .contact-row { display: flex; align-items: center; gap: 16px; }
  .contact-item {
    display: flex; align-items: center; gap: 6px;
    font-size: 11px; color: var(--ink); white-space: nowrap;
  }
  .contact-icon { width: 15px; height: 15px; flex: none; }
  .web-tab {
    position: absolute; left: 150px; top: 339px; width: 344px; height: 46px;
    background: var(--brand-blue); border-radius: 12px 12px 0 0;
    display: flex; align-items: center; justify-content: center;
    color: #fff; font-size: 13px; letter-spacing: 2px;
  }
  .web-tab b { font-weight: 700; }

  /* Back */
  .card-back {
    left: 269px; top: 473px; width: 652px; height: 380px;
    background: radial-gradient(ellipse at 50% 40%, #3d7fc0 0%, var(--brand-blue) 45%, var(--brand-deep) 100%);
  }
  .back-brand {
    position: absolute; left: 0; right: 0; top: 218px; text-align: center;
  }
  .back-brand .brand-name { color: #fff; font-size: 50px; }
  .back-brand .brand-tagline {
    color: var(--tagline-light); font-size: 18px; letter-spacing: 2.4px; margin-top: 2px;
  }
</style>
</head>
<body>
<main class="stage">

  <section class="card card-front" aria-label="Business card front">
    <div class="front-brand">
      <div class="brand-name">Forge Vexa</div>
      <div class="brand-tagline">SHAPING WITH PRECISION</div>
    </div>

    <p class="person-name">Gerald Pinwick</p>

    <div class="contact-list">
      <div class="contact-row">
        <span class="contact-item">
          <svg class="contact-icon" viewBox="0 0 16 16"><circle cx="8" cy="8" r="8" fill="var(--icon-grey)"/><path d="M8 3.5a3 3 0 0 0-3 3c0 2.3 3 5.8 3 5.8s3-3.5 3-5.8a3 3 0 0 0-3-3zm0 4.2a1.2 1.2 0 1 1 0-2.4 1.2 1.2 0 0 1 0 2.4z" fill="#fff"/></svg>
          27615 Harlow Ave Unit C Longmont, CO 80519
        </span>
        <span class="contact-item">
          <svg class="contact-icon" viewBox="0 0 16 16"><circle cx="8" cy="8" r="8" fill="var(--icon-grey)"/><path d="M5.2 4.2l1.4-.4 1 2-0.9.8a5 5 0 0 0 2.7 2.7l.8-.9 2 1-.4 1.4c-3.8.2-6.8-2.8-6.6-6.6z" fill="#fff"/></svg>
          555-204-0147
        </span>
      </div>
      <div class="contact-row">
        <span class="contact-item">
          <svg class="contact-icon" viewBox="0 0 16 16"><circle cx="8" cy="8" r="8" fill="var(--brand-blue)"/><rect x="5.5" y="3.5" width="5" height="9" rx="1" fill="#fff"/><rect x="6.5" y="4.8" width="3" height="5.4" fill="var(--brand-blue)"/></svg>
          555-318-0182
        </span>
        <span class="contact-item">
          <svg class="contact-icon" viewBox="0 0 16 16"><circle cx="8" cy="8" r="8" fill="var(--icon-grey)"/><rect x="4" y="5" width="8" height="6" rx="0.8" fill="#fff"/><path d="M4.3 5.4L8 8.3l3.7-2.9" fill="none" stroke="var(--icon-grey)" stroke-width="0.9"/></svg>
          gpinwick@forgevx.com
        </span>
        <span class="contact-item">
          <svg class="contact-icon" viewBox="0 0 16 16"><circle cx="8" cy="8" r="8" fill="var(--icon-grey)"/><g fill="none" stroke="#fff" stroke-width="0.9"><circle cx="8" cy="8" r="4"/><ellipse cx="8" cy="8" rx="1.8" ry="4"/><path d="M4 8h8"/></g></svg>
          www.forgevx.com
        </span>
      </div>
    </div>

    <div class="web-tab">www.<b>forgevx</b>.com</div>
  </section>

  <section class="card card-back" aria-label="Business card back">
    <div class="back-brand">
      <div class="brand-name">Forge Vexa</div>
      <div class="brand-tagline">SHAPING WITH PRECISION</div>
    </div>
  </section>

</main>
</body>
</html>
```